Etiketten-Design für Weißwein
Zielgruppe
Wir betreiben einen Weingroßhandel, beliefern die Gastronomie mit Wein und haben einen Onlineshop unter kerstel-wein.de
Zielgruppe für diesen Wein: Gastronomie und Privatkunden, Altersgruppe: 25-40, Charakteristiken: jung, aufgeschlossen und lebenslustig.
Aufgabenstellung
Zum Produkt: Flaschenform Bordeauxflasche, Inhalt Weißwein feinherb und wertig von einem Top Weingut, als Sommerwein gedacht.
Das Etikett soll modern sein und auffallen. Unsere erste Idee war MIRAVELLO mit einem Spruch: Kein Ziel, kein Plan, aber fantastischen Wein. Wir freuen uns aber auch über neue Ideen.
u.U. könnten weitere Weine mit diesem Etikett mit leichten Anpassungen entstehen (z.B. ein Rotwein und ein Rose)

```html
<!DOCTYPE html>
<html lang="de">
<head>
<meta charset="utf-8">
<title>MIRAVELLO – Weißwein Etikett</title>
<link rel="stylesheet" href="https://fonts.googleapis.com/css2?family=Fira+Sans+Condensed:wght@400;500;600&display=swap">
<style>
  :root {
    --page-bg: #ffffff;
    --label-bg: #3e4049;
    --label-ink: #ffffff;
    --rule: #e9e9ec;
  }
  html, body {
    margin: 0;
    padding: 0;
    width: 1200px;
    height: 1200px;
    overflow: hidden;
    background: var(--page-bg);
  }
  .canvas {
    position: relative;
    width: 1200px;
    height: 1200px;
  }
  .wine-label {
    position: absolute;
    left: 167px;
    top: 105px;
    width: 866px;
    height: 991px;
    background: var(--label-bg);
    color: var(--label-ink);
    font-family: "Fira Sans Condensed", "Arial Narrow", sans-serif;
    text-align: center;
  }
  .wine-name {
    position: absolute;
    left: 0;
    right: 0;
    top: 84px;
    margin: 0;
    font-size: 150px;
    font-weight: 500;
    line-height: 146px;
    letter-spacing: 3px;
  }
  .wine-name span { display: block; }
  .slogan {
    position: absolute;
    left: 0;
    right: 0;
    top: 458px;
    margin: 0;
    font-size: 56px;
    font-weight: 500;
    line-height: 72px;
    letter-spacing: 2px;
  }
  .slogan span { display: block; }
  .divider {
    position: absolute;
    left: 101px;
    top: 688px;
    width: 661px;
    height: 3px;
    background: var(--rule);
    border: 0;
    margin: 0;
  }
  .wine-details {
    position: absolute;
    left: 0;
    right: 0;
    top: 780px;
    margin: 0;
    font-size: 46px;
    font-weight: 400;
    line-height: 62px;
    letter-spacing: 2px;
  }
  .wine-details span { display: block; }
</style>
</head>
<body>
  <main class="canvas">
    <section class="wine-label" aria-label="Weinetikett MIRAVELLO">
      <h1 class="wine-name"><span>MIRA</span><span>VELLO</span></h1>
      <p class="slogan"><span>KEIN ZIEL, KEIN PLAN,</span><span>ABER FANTASTISCHEN WEIN</span></p>
      <hr class="divider">
      <p class="wine-details"><span>WEISSWEIN – FEINHERB</span><span>2020</span></p>
    </section>
  </main>
</body>
</html>
```